International Property Consultancy

Brief Overview:

I need a dynamic and well designed website that is easy to use and understand. It has to be unique and different to generic templates that most websites seem to be these days. PLEASE NO GENERIC TEMPLATES FROM THE INTERNET.

Our business has 10 years experience working on struggling international developments that we then work in-house for to turn around and brings bout success. We stay within a project often for long periods of time until success is achieved. We are unique in our approach and completely different to the standard routes to market for many developments. The site is for developers to see what we have done in regards to previous projects, as such we want to incorporate video into this site with a strong design aesthetic. There will be videos of the past projects we have worked on, which will act as case studies.

I like very simple but punchy websites, that people can navigate and understand very easily. Also a big fan of unique and well thought out design aesthetic.

Initial Site layout thoughts:

1) Homepage:
2) About Us
3) What we've done / Work
This part has the projects we have worked on (France, Portugal, London, Morocco). Each one will have some video content and photo images, but also would be good to have a succinct way to mention what we did and the successes in a clever and punchy way.

4) Contact Us

* This is just a guideline. Would be open to input and creative direction on your own part.

*More details and websites we like can be seen in the brief doc attached.

PLEASE VIEW THE WIREFRAME WORD DOC ATTACHED.

Here there are also some more examples to help:

Here are just a few examples of websites and what I like about them:

- www.velmoro.com (clean, nice geometric design aesthetic, good animation when loading and changing pages well thought out all though also coulee be considered a bit dull and basic after the initial homepage slide)
- https://www.farbridgehub.net (Clean site, quite clinical, lacks video content and doesn't engage greatly).
- https://ruskotile.com (minimal, and like how it mixes the design aesthetic more with video and photo content)

- https://www.amberquillworks.com (like the layout of this and how it displays the projects and work section)

- https://brisk.com (Good use of video content)

- https://loomfield.studio (minimal to the point and mixes design with video and animation etc...)

Here is another couple of cool websites that may help give you some direction: https://halvenquay.com www.brisk.com

Hi there, One of the things I thought would be good on the homepage is to add the logo with a 'digital landscape' before flicking down into a slide with video content of the projects... Just an idea but have posted some pics in the brief. We would get this animated for the site. But if you have better ideas, please do run with them. Thanks,

Target Market(s)

Property developers

Number of Pages Required

4 page

Font styles to use
Other font styles liked:
• Read brief

Requirements
Must have
• Needs to be clean, dynamic and easy to follow on desktop and mobile. We will use it as a kind of portfolio website so will need to embed video of past projects we have worked on.

Read brief in docs.
Nice to have
• Clean
Should not have
• Not be another generic template website.
Not have random property stock photos. (We are not a property agency).

```html
<!DOCTYPE html>
<html lang="en">
<head>
<meta charset="utf-8">
<title>calveren. — International Property Consultancy</title>
<link href="https://fonts.googleapis.com/css2?family=Quicksand:wght@600;700&family=Lato:wght@400;700&display=swap" rel="stylesheet">
<style>
:root{
  --ink:#0f2330;
  --text:#555b60;
  --muted:#6b7075;
  --peach:#f9e3da;
  --peach-line:#f6c9a8;
  --teal:#134657;
  --white:#ffffff;
}
*{margin:0;padding:0;box-sizing:border-box}
html,body{width:1200px;height:3915px;overflow:hidden;background:var(--white)}
body{position:relative;font-family:"Lato",sans-serif;color:var(--ink)}
.abs{position:absolute}
.brand{font-family:"Quicksand",sans-serif;font-weight:700;color:var(--ink);letter-spacing:-0.5px;line-height:1}
.nav-logo{left:97px;top:30px;font-size:36px}
.nav-links{left:321px;top:42px;display:flex;gap:20px;font-size:13px;font-weight:700;text-transform:uppercase}
.btn{position:absolute;display:flex;align-items:center;justify-content:center;gap:10px;border-radius:24px;font-size:13px;font-weight:700;text-transform:uppercase}
.btn-dark{background:var(--ink);color:var(--white)}
.btn-light{background:var(--peach);color:var(--ink)}
.btn svg{width:13px;height:13px}
.hero-logo{left:0;width:1200px;top:190px;text-align:center;font-size:92px}
.landscape{left:0;top:300px;width:1200px;height:300px;background:radial-gradient(ellipse at 50% 30%,rgba(246,201,168,.55),rgba(249,227,218,.25) 55%,rgba(255,255,255,0) 80%)}
.play-hero{left:568px;top:310px}
.scroll-hint{left:1130px;top:505px;font-size:12px;font-weight:700;transform:rotate(-90deg);transform-origin:left top;top:562px}
.section-title{font-family:"Quicksand",sans-serif;font-weight:700;font-size:52px;color:var(--ink);letter-spacing:-0.5px}
.recent-title{left:0;width:1200px;top:672px;text-align:center}
.media{position:absolute;width:386px;height:477px}
.media .tag{position:absolute;right:12px;bottom:16px;font-size:27px;color:var(--white)}
.media .play{position:absolute;left:178px;top:223px}
.project-title{font-family:"Quicksand",sans-serif;font-weight:700;font-size:48px;color:var(--ink);position:absolute}
.project-text{position:absolute;width:390px;font-size:19px;line-height:30px;color:var(--text)}
.steps{left:1131px;top:985px;font-size:12px;font-weight:700}
.about-art{left:155px;top:3057px;width:320px;height:363px;background:linear-gradient(180deg,var(--peach) 0%,var(--teal) 20%,var(--teal) 70%,var(--ink) 82%,var(--peach) 100%)}
.about-title{left:587px;top:3085px}
.about-text{left:592px;top:3172px;width:520px;font-size:18px;line-height:38px;color:var(--text)}
.footer-col h4{font-size:14px;font-weight:700;text-transform:uppercase;margin-bottom:18px}
.footer-col li{list-style:none;font-size:14px;color:var(--muted);height:34px;display:flex;gap:14px}
.footer-col li::before{content:"»";color:var(--ink)}
.foot-logo{left:703px;top:3580px;font-size:88px}
.socials{left:911px;top:3678px;display:flex;gap:7px}
.socials span{width:38px;height:38px;border:2px solid var(--ink);border-radius:50%}
.rule{left:0;top:3795px;width:1200px;height:1px;background:#e6e6e6}
.copy{left:762px;top:3851px;font-size:14px;color:var(--muted)}
</style>
</head>
<body>

<header>
  <div class="abs brand nav-logo">calveren.</div>
  <nav class="abs nav-links"><span>Home</span><span>About us</span><span>Recent projects</span><span>Contact us</span></nav>
  <a class="btn btn-dark" style="left:763px;top:27px;width:203px;height:46px">Create an account
    <svg viewBox="0 0 16 16"><circle cx="8" cy="8" r="7" fill="none" stroke="#fff" stroke-width="1.6"/><circle cx="8" cy="6.3" r="2.4" fill="#fff"/><path d="M3.8 12.6c1-1.9 2.4-2.6 4.2-2.6s3.2.7 4.2 2.6" fill="#fff"/></svg></a>
  <a class="btn btn-light" style="left:978px;top:27px;width:125px;height:46px">Log in
    <svg viewBox="0 0 16 16"><rect x="3" y="7" width="10" height="8" rx="1" fill="#0f2330"/><path d="M5 7V5a3 3 0 0 1 6 0v2" fill="none" stroke="#0f2330" stroke-width="1.8"/></svg></a>
</header>

<section class="hero">
  <div class="abs landscape" role="img" aria-label="Soft peach digital wireframe landscape"></div>
  <div class="abs brand hero-logo">calveren.</div>
  <svg class="abs play-hero" width="64" height="64" viewBox="0 0 64 64"><circle cx="32" cy="32" r="30" fill="#134657" stroke="#7b98a6" stroke-width="4"/><path d="M26 21l17 11-17 11z" fill="#fff"/></svg>
  <div class="abs scroll-hint">SCROLL</div>
  <svg class="abs" style="left:1139px;top:578px" width="12" height="26" viewBox="0 0 12 26"><path d="M6 0v24M1 19l5 6 5-6" fill="none" stroke="#888" stroke-width="1.5"/></svg>
</section>

<section class="projects">
  <h2 class="abs section-title recent-title">recent projects</h2>

  <div class="abs steps">01.</div>
  <div class="abs" style="left:1140px;top:1015px;width:1px;height:137px;background:#ddd"></div>
  <div class="abs" style="left:1139px;top:1015px;width:3px;height:34px;background:var(--ink)"></div>
  <div class="abs steps" style="top:1174px">04.</div>

  <article>
    <div class="media" style="left:163px;top:823px;background:linear-gradient(180deg,#8fa6bd 0%,#7c8a72 28%,#3f7f90 45%,#1f6f80 100%)" role="img" aria-label="Video still of a coastal harbour town with boats">
      <svg class="play" width="30" height="30" viewBox="0 0 30 30"><circle cx="15" cy="15" r="14" fill="#fff"/><path d="M12 9l9 6-9 6z" fill="#0f2330"/></svg>
      <span class="brand tag">calveren.</span>
    </div>
    <h3 class="project-title" style="left:650px;top:928px">Portugal Resort</h3>
    <p class="project-text" style="left:652px;top:1007px">Lorem ipsum dolor sit amet, consectetur adipiscing elit, sed do eiusmod tempor incididunt ut labore et dolore magna aliqua. Ut enim ad minim veniam, quis nostrud exercitation ullamco laboris nisi ut aliquip ex ea commodo consequat.</p>
  </article>

  <article>
    <div class="media" style="left:653px;top:1381px;background:linear-gradient(180deg,#9aa3a0 0%,#b9ad98 35%,#a49880 60%,#7d705f 100%)" role="img" aria-label="Video still of a city skyline with a tall minaret at dusk">
      <svg class="play" width="30" height="30" viewBox="0 0 30 30"><circle cx="15" cy="15" r="14" fill="#fff"/><path d="M12 9l9 6-9 6z" fill="#0f2330"/></svg>
      <span class="brand tag">calveren.</span>
    </div>
    <h3 class="project-title" style="left:160px;top:1486px">Morocco</h3>
    <p class="project-text" style="left:162px;top:1565px">Lorem ipsum dolor sit amet, consectetur adipiscing elit, sed do eiusmod tempor incididunt ut labore et dolore magna aliqua. Ut enim ad minim veniam, quis nostrud exercitation ullamco laboris nisi ut aliquip ex ea commodo consequat.</p>
  </article>

  <article>
    <div class="media" style="left:163px;top:1943px;background:linear-gradient(180deg,#6e7378 0%,#8a9195 30%,#4e5d68 60%,#8b8b86 100%)" role="img" aria-label="Video still of a financial district skyline under cloudy sky">
      <svg class="play" width="30" height="30" viewBox="0 0 30 30"><circle cx="15" cy="15" r="14" fill="#fff"/><path d="M12 9l9 6-9 6z" fill="#0f2330"/></svg>
      <span class="brand tag">calveren.</span>
    </div>
    <h3 class="project-title" style="left:650px;top:2046px">London</h3>
    <p class="project-text" style="left:652px;top:2126px">Lorem ipsum dolor sit amet, consectetur adipiscing elit, sed do eiusmod tempor incididunt ut labore et dolore magna aliqua. Ut enim ad minim veniam, quis nostrud exercitation ullamco laboris nisi ut aliquip ex ea commodo consequat.</p>
  </article>

  <article>
    <div class="media" style="left:653px;top:2500px;background:linear-gradient(180deg,#5d93c8 0%,#9db9cf 30%,#b2ada0 55%,#3f6a5a 80%,#2e5a3c 100%)" role="img" aria-label="Aerial video still of a city with a river and iron tower">
      <svg class="play" width="30" height="30" viewBox="0 0 30 30"><circle cx="15" cy="15" r="14" fill="#fff"/><path d="M12 9l9 6-9 6z" fill="#0f2330"/></svg>
      <span class="brand tag">calveren.</span>
    </div>
    <h3 class="project-title" style="left:160px;top:2604px">France</h3>
    <p class="project-text" style="left:162px;top:2684px">Lorem ipsum dolor sit amet, consectetur adipiscing elit, sed do eiusmod tempor incididunt ut labore et dolore magna aliqua. Ut enim ad minim veniam, quis nostrud exercitation ullamco laboris nisi ut aliquip ex ea commodo consequat.</p>
  </article>
</section>

<section class="about">
  <div class="abs about-art" role="img" aria-label="Geometric illustration of a house shape in teal and peach"></div>
  <h2 class="abs section-title about-title">about us</h2>
  <p class="abs about-text">Sed ut perspiciatis unde omnis iste natus error sit voluptatem accusantium doloremque laudantium totam rem aperiam, eaque ipsa quae ab illo inventore veritatis et quasi architecto beatae vitae dicta sunt explicabo.</p>
  <a class="btn btn-dark" style="left:592px;top:3338px;width:165px;height:48px">Read more
    <svg viewBox="0 0 16 16"><circle cx="8" cy="8" r="7" fill="#fff"/><path d="M6.5 4.5L10 8l-3.5 3.5" fill="none" stroke="#0f2330" stroke-width="2"/></svg></a>
</section>

<footer>
  <div class="abs footer-col" style="left:115px;top:3545px">
    <h4>Quick links</h4>
    <ul><li>Home</li><li>About us</li><li>Recent Projects</li><li>Reviews</li><li>Contact us</li></ul>
  </div>
  <div class="abs footer-col" style="left:373px;top:3545px">
    <h4>Other links</h4>
    <ul><li>FAQ</li><li>Privacy Policy</li><li>Terms &amp; Conditions</li><li>Help Service</li><li>Contact us</li></ul>
  </div>
  <div class="abs brand foot-logo">calveren.</div>
  <div class="abs socials"><span></span><span></span><span></span><span></span></div>
  <div class="abs rule"></div>
  <a class="btn btn-dark" style="left:112px;top:3838px;width:203px;height:45px">Create an account
    <svg viewBox="0 0 16 16"><circle cx="8" cy="8" r="7" fill="none" stroke="#fff" stroke-width="1.6"/><circle cx="8" cy="6.3" r="2.4" fill="#fff"/><path d="M3.8 12.6c1-1.9 2.4-2.6 4.2-2.6s3.2.7 4.2 2.6" fill="#fff"/></svg></a>
  <a class="btn btn-light" style="left:327px;top:3838px;width:125px;height:45px">Log in
    <svg viewBox="0 0 16 16"><rect x="3" y="7" width="10" height="8" rx="1" fill="#0f2330"/><path d="M5 7V5a3 3 0 0 1 6 0v2" fill="none" stroke="#0f2330" stroke-width="1.8"/></svg></a>
  <p class="abs copy">© 2020 Calveren. All Rights Reserved</p>
</footer>

</body>
</html>
```